Personal Development Book for Millennials Needs a Cover Design

Book Title: Salt Horizon: A Dreamer's Map to Being, 15 "No Escape" Queries on Joy, Routines and Grit for Muddled Millennials
Author's Name: Marcus T. Oldenfrey
Salt Horizon: A Dreamer's Map to Being is a collection of raw, unfiltered and personal essays on happiness, habits and hustle. It is a compilation of 15 provocative, yet fundamental questions that every mixed-up millennial or twenty-something should answer in order to live a life full of energy and excitement rather than monotony and mediocrity.
It is a personal development book written by a regular, twenty-something dude who got tired of doing boring things. He then quit his job, fell off a motorcycle somewhere near the equator, and came back to the States and immediately started writing.
"Pura vida," the law of the land in Costa Rica, translates to "pure life." "Pura vida" is more than just a greeting; it is an embodiment of the Costa Rican people, who find immense happiness in life's little pleasures, preferring to lay low, live slow and live purposefully. "Pura vida" is another way of saying "relax and take it easy."
The goal of the book is to stand out on the Zelvora platform as a small thumbnail. The imagery should make the viewer feel that the book (and the author) is an authority on the topic of self-discovery, self-awareness, and purposeful, intentional living.
The reader should feel that they MUST read this book if they are the least bit confused, anxious, mixed-up or desperately trying to figure out how to take back control of their own life and start doing the things that excite them. It's more important that the book "pops off the shelf" or stands out and catches the eye quickly.
The most important part of the design is that it is clean, uncluttered and simple. It should embody the "pura vida" lifestyle. I am open to any image or illustration you choose.
I like a bold color palette, and I'd like to see green be the primary color used in the design. Lush, greenery is everywhere in Costa Rica. Green also represents life, very appropriate for this book. I like bold titles that are easy to recognize and comprehend. Please use no more than 2-3 colors.
Zelvora eBook covers I particularly like:
Print Liftoff by Wesley Harrow
A Man Near The Pier by Neil Dorsey
Inner Steel — 48 Tested Paths to Build Inner Steel, Lift Your Morale and Quiet Inner Worry by Rory M.T. Pask
Hour Mastery: Peak Output by Owen Farrukh
Target Market(s)
Millennials
Requirements
Must have
- This book is intended to encourage millennials to do some soul-searching, think and WRITE down their own answers to the questions in this book. It is a book that should be read with a notebook and a pen close by.
- I'd like to see covers that subtly hint at this fact. Please reference the example covers listed in the project description to best match the style of cover I am looking for. If it is clear that you have NOT referenced the example covers, your design will be eliminated.
Nice to have
- If possible, would like to see designs that include the following three components WITHOUT making the cover feel too busy or cluttered:
- 1) Pen
- 2) Paper
- 3) Beach
Should not have
- Cover should NOT look or feel as if this is a book about environmentalism. Trees, plants, greenery, etc. should NOT be the primary focal point of the cover design. If included, these elements should be additive.

```html
<!DOCTYPE html>
<html lang="en">
<head>
<meta charset="utf-8">
<title>Salt Horizon – Marcus T. Oldenfrey</title>
<link href="https://fonts.googleapis.com/css2?family=Passion+One:wght@700&family=Patrick+Hand+SC&display=swap" rel="stylesheet">
<style>
  :root {
    --sky: #5fb0e6;
    --sky-pale: #cfe8f8;
    --paper: #ffffff;
    --title-stroke: #2f8fd2;
    --title-fill: #e6f4fd;
    --ink: #151515;
    --tile-slate: #b9c6d3;
    --tile-grey: #c7c3bc;
    --tile-sand: #e8c79a;
    --tile-peach: #f4b76c;
    --tile-orange: #f9a11b;
    --band-amber: rgba(246, 178, 92, 0.45);
    --band-yellow: rgba(255, 233, 120, 0.35);
    --sun: #ffe100;
    --leaf: #5fbf3b;
    --leaf-pale: #cfeabe;
    --author-text: #f4ffd8;
  }
  html, body { margin: 0; padding: 0; overflow: hidden; background: #e9e9e9; }
  .cover {
    position: relative;
    width: 800px;
    height: 1200px;
    overflow: hidden;
    background: linear-gradient(180deg, var(--sky) 0%, var(--sky-pale) 22%, var(--paper) 45%, var(--paper) 100%);
  }
  .cover::before {
    content: "";
    position: absolute; inset: 0;
    background: linear-gradient(90deg, rgba(95,176,230,0.55) 0%, rgba(255,255,255,0) 55%);
  }
  .tile { position: absolute; }
  .tile-row .tile { top: 18px; width: 56px; height: 56px; }
  .t1 { left: 475px; background: var(--tile-slate); opacity: .8; }
  .t2 { left: 539px; background: var(--tile-grey); opacity: .9; }
  .t3 { left: 603px; background: var(--tile-sand); }
  .t4 { left: 667px; background: var(--tile-peach); }
  .t5 { left: 731px; background: var(--tile-orange); }
  .band-horizontal {
    position: absolute; left: 0; right: 0; top: 92px; height: 30px;
    background: var(--band-yellow);
  }
  .band-vertical {
    position: absolute; left: 520px; width: 54px; top: 0; height: 890px;
    background: linear-gradient(180deg, var(--band-amber) 0%, rgba(246,178,92,0.25) 70%, rgba(246,178,92,0) 100%);
  }
  .band-vertical.slim {
    left: 600px; width: 22px; height: 600px;
    background: linear-gradient(180deg, rgba(249,161,27,0.3), rgba(249,161,27,0));
  }
  .sun-stack .tile { left: 0; width: 78px; height: 60px; background: var(--sun); }
  .s1 { top: 372px; }
  .s2 { top: 440px; opacity: .7; }
  .s3 { top: 508px; opacity: .45; }
  .s4 { top: 576px; opacity: .28; }
  .s5 { top: 644px; opacity: .14; }
  .leaf-stack .tile { left: 690px; width: 96px; height: 60px; background: var(--leaf); }
  .l1 { top: 770px; opacity: .12; }
  .l2 { top: 838px; opacity: .2; }
  .l3 { top: 906px; opacity: .3; }
  .l4 { top: 974px; opacity: .42; }
  .l5 { top: 1110px; opacity: .55; height: 70px !important; }
  .title {
    position: absolute; left: 0; right: 0; top: 150px; margin: 0;
    text-align: center;
    font-family: "Passion One", "Arial Black", sans-serif;
    font-weight: 700;
    font-size: 118px;
    line-height: 1;
    letter-spacing: 4px;
    color: var(--title-fill);
    -webkit-text-stroke: 4px var(--title-stroke);
    text-transform: uppercase;
  }
  .subtitle {
    position: absolute; left: 0; right: 0; top: 325px; margin: 0;
    text-align: center;
    font-family: "Patrick Hand SC", "Comic Sans MS", cursive;
    font-size: 40px;
    line-height: 1.2;
    color: var(--ink);
    letter-spacing: 1px;
  }
  .subtitle span { display: block; }
  .author-band {
    position: absolute; left: 0; top: 1078px; width: 690px; height: 76px;
    background: var(--leaf);
    display: flex; align-items: center; justify-content: center;
  }
  .author {
    margin: 0;
    font-family: "Patrick Hand SC", "Comic Sans MS", cursive;
    font-size: 52px;
    letter-spacing: 2px;
    color: var(--author-text);
  }
</style>
</head>
<body>
  <main class="cover">
    <div class="band-horizontal"></div>
    <div class="band-vertical"></div>
    <div class="band-vertical slim"></div>
    <div class="tile-row">
      <div class="tile t1"></div><div class="tile t2"></div><div class="tile t3"></div><div class="tile t4"></div><div class="tile t5"></div>
    </div>
    <div class="sun-stack">
      <div class="tile s1"></div><div class="tile s2"></div><div class="tile s3"></div><div class="tile s4"></div><div class="tile s5"></div>
    </div>
    <div class="leaf-stack">
      <div class="tile l1"></div><div class="tile l2"></div><div class="tile l3"></div><div class="tile l4"></div><div class="tile l5"></div>
    </div>
    <h1 class="title">Salt Horizon</h1>
    <p class="subtitle">
      <span>A Dreamer's Map to Being –</span>
      <span>15 "No Escape" Queries on</span>
      <span>Joy, Routines and Grit</span>
      <span>for Muddled Millennials</span>
    </p>
    <div class="author-band">
      <p class="author">Marcus T. Oldenfrey</p>
    </div>
  </main>
</body>
</html>
```